Packaging Design for Vorimelt a Company Providing a Convenient and Complete Alternative to Food

We need a packaging and label design for Vorimelt. Vorimelt stands for nutrient balance and it is a meal alternative that comes in a powder that has all the nutrients needed for a complete and balanced meal. Vorimelt would be used by people that are hungry but don't have time to cook, are in a rush, or simply want to get the healthiest meal they can as conveniently as possible. We were thinking of using a modern and simple design that would attract consumers in the 22-28 age bracket. I want the packaging to be cool and attractive using blue and orange/red (an orangey red) since those are the colors of the logo

Now that being said, Vorimelt is more about a lifestyle than the product itself. The website still doesn't reflect this because the first step for me in creating it was to put in all the hard info and facts and then slowly transform it to what I want it to be. Vorimelt's "slogan" is spark every hour and the idea is that the product will be used by people who are busy having too much fun in life so they don't have time to cook so they choose to have Vorimelt. For example a commercial we are producing starts with first person footage of me getting in a skyvane 40 and then doing all sorts of water sports and having fun in the beach. At the end, there's a hot girl in a boat making a vorimelt and drinking it. So as you can see it's not about the product itself but what we want people to feel when they think about it and part of what they feel will be conveyed by the logo.

I want to convey a sense of energy and fun. I want people to feel inspired and feel something when they see the packaging since this is the same logo that will go on the product packaging (I will hold another project for that as soon as this one ends).

Our target market is a young professional probably with higher disposable income than your average 24-35 year old, trendy, modern, sophisticated and often consumes premium brands and therefore the packaging must reflect that.

The bottle will use a shrink sleeve that will wrap around from the bottom of the bottle up to the neck. The bottle is white, with a white smooth cap. I want the design to be able to blend in with the white of the bottle so that it all flows. I was thinking of maybe leaving some parts transparent so that the white of the bottle shows instead of using white but I honestly don't know if that would be a good idea.

Attached you will find the template for the shrink sleeve, the logo and the tub. The picture of the bottle is only a reference so that you can know what size it will be.

I'm going to need the design both in the template and on the tub. Make it look nice since I might be using the designs as a background in the website and definitely as the product image (what people will be clicking on to buy it)

Here are the things that need to be on the tub (these will be modified later only to be used as a placeholder for now):

Under the logo or in the front and middle of the tub (under Vorimelt probably):
A Complete and Balanced Meal Alternative.

It needs to say its vanilla flavored

It needs to have the supplement facts (just put any random numbers)

Directions: Use 2-4 scoops depending on your level of hunger. Mix 5 ounces of water per scoop in a thermos, shaker cup, or closed bottle and shake vigorously for ten seconds. Drink and enjoy!

What is Vorimelt?
Vorimelt is a complete and balanced meal alternative that gives your body all the right nutrients to keep it functioning at its full potential. Vorimelt will nourish your body with good proteins, carbohydrates, fats, and micro-nutrients (like vitamins and minerals) so that you don't have to worry about cooking or eating the right stuff. We take care of everything for you so that you can keep on doing what you love, whatever that may be. Vorimelt will spark every hour!
For more information go to Vorimelt.example

Hey i forgot to add that its gonna be vanilla flavored

```html
<!DOCTYPE html>
<html lang="en">
<head>
<meta charset="utf-8">
<title>Vorimelt Vanilla Label</title>
<link rel="stylesheet" href="https://fonts.googleapis.com/css2?family=Permanent+Marker&family=Roboto:wght@500;700&family=Roboto+Condensed:wght@700&display=block">
<style>
  :root {
    --backdrop: #b4b4b4;
    --label-white: #f4f4f4;
    --brand-blue: #1a6fa8;
    --sky-blue: #2794c4;
    --deep-blue: #15609a;
    --flame-orange: #e14d0c;
    --amber-orange: #ec6a12;
    --ink-dark: #333333;
    --flavor-orange: #d4500e;
  }
  html, body {
    margin: 0;
    padding: 0;
    width: 1200px;
    height: 1200px;
    overflow: hidden;
    background: var(--backdrop);
  }
  .canvas {
    position: relative;
    width: 1200px;
    height: 1200px;
    background: radial-gradient(circle at 50% 45%, #dcdcdc 0%, var(--backdrop) 70%);
  }
  .sleeve-label {
    position: absolute;
    left: 100px;
    top: 240px;
    width: 1000px;
    height: 720px;
    background: var(--label-white);
    overflow: hidden;
    box-shadow: 0 10px 30px rgba(0,0,0,0.18);
  }
  .sleeve-art {
    position: absolute;
    inset: 0;
  }
  .brand-block {
    position: absolute;
    left: 0;
    right: 0;
    top: 150px;
    text-align: center;
  }
  .brand-dot {
    display: block;
    width: 150px;
    height: 150px;
    margin: 0 auto 28px;
    border-radius: 50%;
    background: var(--brand-blue);
  }
  .brand-name {
    margin: 0;
    font-family: "Roboto", Arial, sans-serif;
    font-weight: 500;
    font-size: 104px;
    letter-spacing: 3px;
    line-height: 1;
    color: var(--brand-blue);
    text-transform: uppercase;
  }
  .tagline {
    margin: 16px 0 0;
    font-family: "Roboto Condensed", "Roboto", Arial, sans-serif;
    font-weight: 700;
    font-size: 26px;
    color: var(--ink-dark);
  }
  .flavor-callout {
    position: absolute;
    right: 120px;
    top: 505px;
    margin: 0;
    font-family: "Permanent Marker", "Comic Sans MS", cursive;
    font-size: 42px;
    line-height: 1;
    letter-spacing: 1px;
    color: var(--flavor-orange);
    transform: rotate(-9deg);
    transform-origin: right center;
    white-space: nowrap;
  }
</style>
</head>
<body>
<main class="canvas">
  <section class="sleeve-label">
    <svg class="sleeve-art" viewBox="0 0 1000 720" width="1000" height="720" aria-hidden="true">
      <defs>
        <linearGradient id="orangeSweep" x1="0" y1="1" x2="1" y2="0">
          <stop offset="0" stop-color="#ec6a12"/>
          <stop offset="1" stop-color="#e14d0c"/>
        </linearGradient>
        <linearGradient id="blueSweep" x1="0" y1="0" x2="1" y2="1">
          <stop offset="0" stop-color="#2794c4"/>
          <stop offset="1" stop-color="#15609a"/>
        </linearGradient>
      </defs>
      <path class="orange-swoosh" d="M0 0 H330 C300 160 190 290 0 360 Z" fill="url(#orangeSweep)"/>
      <path class="blue-arc" d="M800 0 H860 C930 140 975 300 1000 470 V580 C960 370 900 170 800 0 Z" fill="url(#blueSweep)"/>
      <path class="blue-band" d="M0 640 C300 690 650 680 1000 590 V720 H0 Z" fill="url(#blueSweep)"/>
      <path class="blue-band-shade" d="M0 672 C300 715 650 705 1000 640 V720 H0 Z" fill="#15609a" opacity="0.55"/>
    </svg>

    <div class="brand-block">
      <span class="brand-dot"></span>
      <h1 class="brand-name">Vorimelt</h1>
      <p class="tagline">A Complete and Balanced Meal Alternative.</p>
    </div>

    <p class="flavor-callout">Vanilla Flavored!</p>
  </section>
</main>
</body>
</html>
```